Important Solar Energy Company Needs a Stationery Design

I need a modern, attractive, corporate stationary design (letter head and business card)
Attached Company Logo

Target Market(s)

Upmarket

Industry/Entity Type

Business

Colors
ec1f27
ffffff
757575
cbcbcb
000000

```html
<!DOCTYPE html>
<html lang="en">
<head>
<meta charset="utf-8">
<title>Solariva Business Card</title>
<link rel="stylesheet" href="https://fonts.googleapis.com/css2?family=Didact+Gothic&family=Montserrat:wght@400;700&display=swap">
<style>
  :root {
    --brand-red: #ec1f27;
    --brand-red-deep: #b8151c;
    --white: #ffffff;
    --grey-mid: #757575;
    --grey-light: #cbcbcb;
    --ink: #000000;
    --backdrop: #2a2a2a;
  }
  * { box-sizing: border-box; margin: 0; padding: 0; }
  html, body { width: 1200px; height: 768px; overflow: hidden; }
  body {
    background: var(--backdrop);
    display: flex;
    align-items: center;
    justify-content: center;
    gap: 56px;
    font-family: "Didact Gothic", sans-serif;
  }
  .card {
    width: 525px;
    height: 300px;
    border-radius: 16px;
    position: relative;
    overflow: hidden;
  }
  .card-back {
    background: linear-gradient(135deg, #f4f4f4 0%, #e2e2e2 55%, var(--grey-light) 100%);
    display: flex;
    flex-direction: column;
    align-items: center;
    justify-content: center;
  }
  .brand-dot {
    width: 78px;
    height: 78px;
    border-radius: 50%;
    background: var(--brand-red);
    margin-bottom: 18px;
  }
  .brand-name {
    font-family: "Montserrat", sans-serif;
    font-weight: 400;
    letter-spacing: 4px;
    text-transform: uppercase;
  }
  .card-back .brand-name { color: #333333; font-size: 28px; }
  .card-back .site {
    margin-top: 22px;
    font-size: 12px;
    color: var(--grey-mid);
    letter-spacing: 1px;
  }
  .card-front {
    background: linear-gradient(150deg, var(--brand-red) 0%, #ee3a40 40%, var(--brand-red) 65%, var(--brand-red-deep) 100%);
    color: var(--white);
    padding: 26px 30px;
  }
  .card-front .brand-name { font-size: 24px; color: var(--white); }
  .holder { margin-top: 14px; }
  .holder-name {
    font-family: "Montserrat", sans-serif;
    font-weight: 700;
    font-size: 17px;
  }
  .holder-role { font-size: 14px; margin-top: 2px; }
  .address { margin-top: 14px; font-size: 13px; line-height: 1.3; }
  .contacts { list-style: none; margin-top: 10px; font-size: 13.5px; }
  .contacts li { display: flex; align-items: center; gap: 9px; line-height: 1.45; }
  .contacts svg { width: 13px; height: 13px; fill: var(--white); flex: none; }
</style>
</head>
<body>
  <section class="card card-back" aria-label="Card back">
    <div class="brand-dot"></div>
    <div class="brand-name">Solariva</div>
    <div class="site">www.solariva.com</div>
  </section>

  <section class="card card-front" aria-label="Card front">
    <div class="brand-name">Solariva</div>
    <div class="holder">
      <div class="holder-name">Daniel Reyes</div>
      <div class="holder-role">CEO/Founder</div>
    </div>
    <div class="address">1420 Copper Ridge Road<br>Helio Springs<br>Nevada 89012</div>
    <ul class="contacts">
      <li><svg viewBox="0 0 16 16"><path d="M3 1h3l1.5 4-2 1.3a9 9 0 0 0 4.2 4.2L11 8.5l4 1.5v3a2 2 0 0 1-2 2A12 12 0 0 1 1 3a2 2 0 0 1 2-2z"/></svg>702 555 0148</li>
      <li><svg viewBox="0 0 16 16"><path d="M4 0h8a1 1 0 0 1 1 1v14a1 1 0 0 1-1 1H4a1 1 0 0 1-1-1V1a1 1 0 0 1 1-1zm1 2v10h6V2zm3 11a1 1 0 1 0 0 2 1 1 0 0 0 0-2z"/></svg>702 555 0193</li>
      <li><svg viewBox="0 0 16 16"><path d="M4 1h7l1 2v3H4zM1 7h14v6h-2v2H3v-2H1zm4 5v2h6v-2z"/></svg>702 555 0167</li>
      <li><svg viewBox="0 0 16 16"><path d="M1 3h14v10H1zm1.5 1.5L8 9l5.5-4.5z"/></svg>contact@solariva.com</li>
      <li><svg viewBox="0 0 16 16"><path d="M8 0a8 8 0 1 0 0 16A8 8 0 0 0 8 0zm0 2a6 6 0 0 1 5.7 4H10V4H6v4H2.1A6 6 0 0 1 8 2zm-4 8h4v4a6 6 0 0 1-4-4z"/></svg>www.solariva.com</li>
    </ul>
  </section>
</body>
</html>
```